Lumara Health & Wellness Business Card Design

We would like to create business cards matching with our new logo design. The card should be professional looking but still have a playful side and something that would be eye catching. We are planing to open a luxury medical spa and looking to create a design based on this new logo. We are looking for a design that shows off luxury but not be gold in color. Also, while we are a more female oriented medical center we do have men that come in for our services and it should be be too feminine.

Target Market(s)

Health & Wellness. Medical patients. Luxury spa

Industry/Entity Type

Health And Wellness

Contact Information for Business Card

It should have the logo design in the front of card and back of card should have our contact information. Our current colors are peach/ coral, teal, and gray. We are looking for a modern looking design.

Font styles to use
Script

Colors
32a6d6
e667a6
86cfc6
fece3e

Requirements
Must have
• It should have our logo design. We would prefer to have a more modern look to the card.
Nice to have
• Eye-Catching Design on the personable side but still classy.
Should not have
• At this point we are looking for the best design. It should not have color purple.

```html
<!DOCTYPE html>
<html lang="en">
<head>
<meta charset="utf-8">
<title>Lumara Health &amp; Wellness – Business Card</title>
<link rel="stylesheet" href="https://fonts.googleapis.com/css2?family=Montserrat:wght@300;400&family=Open+Sans:wght@400&display=swap">
<style>
  :root {
    --backdrop: #1b1b1c;
    --card: #262627;
    --silver: #e4e4e4;
    --teal: #86cfc6;
    --white: #f4f4f4;
  }
  * { margin: 0; padding: 0; box-sizing: border-box; }
  html, body {
    width: 1200px; height: 900px; overflow: hidden;
    background: var(--backdrop);
  }
  .canvas {
    width: 1200px; height: 900px;
    display: flex; flex-direction: column;
    align-items: center; justify-content: center; gap: 40px;
  }
  .card {
    width: 700px; height: 400px;
    background: var(--card);
    border-radius: 30px;
    position: relative;
    box-shadow: 0 10px 30px rgba(0,0,0,.45);
  }
  .brand-name {
    font-family: "Montserrat", sans-serif;
    font-weight: 400;
    color: var(--silver);
    letter-spacing: .08em;
    text-transform: uppercase;
    line-height: 1.25;
  }
  .card-front { display: flex; align-items: center; justify-content: center; }
  .card-front .brand-name { font-size: 34px; text-align: center; }
  .card-back { display: flex; align-items: center; }
  .card-back .brand-name {
    width: 330px; padding-left: 56px;
    font-size: 22px; color: var(--silver);
  }
  .divider {
    width: 2px; height: 150px; background: var(--teal);
    margin: 0 30px 0 22px;
  }
  .contact { font-family: "Open Sans", sans-serif; color: var(--white); }
  .person-name {
    font-family: "Montserrat", sans-serif; font-weight: 300;
    font-size: 30px; letter-spacing: .02em; line-height: 1;
  }
  .job-title {
    font-family: "Montserrat", sans-serif; font-weight: 300;
    font-size: 20px; color: var(--teal); margin-top: 6px; margin-bottom: 26px;
  }
  .contact-line {
    display: flex; align-items: center; gap: 14px;
    font-size: 17px; margin-top: 12px;
  }
  .contact-line svg { width: 18px; height: 18px; fill: var(--teal); flex: none; }
</style>
</head>
<body>
<main class="canvas">
  <section class="card card-front">
    <p class="brand-name">Lumara<br>Health &amp; Wellness</p>
  </section>

  <section class="card card-back">
    <p class="brand-name">Lumara<br>Health &amp; Wellness</p>
    <div class="divider"></div>
    <div class="contact">
      <p class="person-name">YOUR NAME</p>
      <p class="job-title">JOB TITLE</p>
      <p class="contact-line">
        <svg viewBox="0 0 20 20" aria-hidden="true"><path d="M2 7c0-2 3-4 8-4s8 2 8 4v1h-4V6.5c-1-.5-2.4-.8-4-.8s-3 .3-4 .8V8H2z"/><path d="M5 9h10l2 7H3z"/></svg>
        000 000 0000
      </p>
      <p class="contact-line">
        <svg viewBox="0 0 20 20" aria-hidden="true"><path d="M2 4h16v12H2z M3 5l7 6 7-6" fill="none" stroke="#86cfc6" stroke-width="1.6"/><path d="M2 4h16l-8 7z"/></svg>
        youremail@lumara-spa.com
      </p>
    </div>
  </section>
</main>
</body>
</html>
```